Accounting Business needs double sided DL flyer design

We need a double sided DL flyer designed,
Front side with logo, web address and our short intro.
Backside to have a list of services.
Our colours are blue and a concrete grey colour. Look at our website for a feel for our colour scheme.
www.lanternwellgroup.com.au
I have included the pic from our website to possibly use but we are also open to new creative ideas.
Target Market(s)
Our target market are proactive business owners, particularly in the wine and hospitality industry.
Industry/Entity Type
Business
Look and feel

```html
<!DOCTYPE html>
<html lang="en">
<head>
<meta charset="utf-8">
<title>Lanternwell Group – DL Flyer</title>
<link href="https://fonts.googleapis.com/css2?family=Exo+2:wght@500;600;700;800&family=Philosopher:wght@400;700&display=swap" rel="stylesheet">
<style>
  :root{
    --navy:#123f82;
    --navy-deep:#0b3474;
    --band:#163f8c;
    --ink:#1c1c1c;
    --text-grey:#3a3a3a;
    --concrete-light:#ecebea;
    --concrete-mid:#d9d8d7;
    --stage:#2b2b2d;
    --white:#ffffff;
  }
  *{margin:0;padding:0;box-sizing:border-box}
  html,body{width:1200px;height:1015px;overflow:hidden;background:var(--stage)}
  .canvas{position:relative;width:1200px;height:1015px}
  .flyer{
    position:absolute;top:53px;width:456px;height:910px;overflow:hidden;
    background:linear-gradient(180deg,var(--concrete-light) 0%,#e6e4e3 45%,var(--concrete-mid) 100%);
    box-shadow:0 6px 18px rgba(0,0,0,.55);
  }
  .flyer--front{left:67px}
  .flyer--back{left:671px}

  .brand{position:absolute;top:55px;left:52px;display:flex;align-items:center;gap:12px}
  .brand__square{width:44px;height:44px;background:var(--navy)}
  .brand__name{font-family:"Exo 2",sans-serif;font-weight:700;font-size:25px;letter-spacing:1.5px;color:var(--navy);text-transform:uppercase}

  .stairs{
    position:absolute;left:0;right:0;top:500px;height:363px;
    background:linear-gradient(180deg,rgba(160,162,170,0) 0%,#a9aab0 30%,#8d8f97 62%,#b9babd 66%,#c6c7c9 100%);
  }

  .headline{position:absolute;left:45px;top:178px;font-family:"Philosopher",sans-serif;color:var(--ink);line-height:1}
  .headline strong{color:var(--navy);font-weight:700}
  .headline__l1{font-size:38px}
  .headline__l1 strong{font-size:70px}
  .headline__l2{font-size:46px;margin-top:6px}
  .headline__l3{font-size:24px;margin-top:14px}
  .headline__l4{font-size:72px;color:var(--navy);font-weight:700;margin-top:4px}

  .services{position:absolute;left:54px;top:148px;font-family:"Exo 2",sans-serif}
  .services__title{font-size:27px;font-weight:700;color:var(--navy);margin-bottom:14px}
  .services__list{list-style:none}
  .services__item{display:flex;align-items:center;gap:12px;font-size:20px;font-weight:600;color:var(--text-grey);height:39.3px}
  .services__bullet{width:12px;height:12px;background:var(--navy);flex:none}

  .cta{position:absolute;left:0;right:0;top:752px;text-align:center;font-family:"Exo 2",sans-serif}
  .cta__label{font-size:36px;font-weight:800;color:var(--navy-deep);letter-spacing:.5px;text-shadow:0 1px 0 #fff}
  .cta__phone{
    display:inline-flex;align-items:center;justify-content:center;margin-top:5px;
    width:348px;height:50px;border-radius:5px;background:var(--navy-deep);
    color:var(--white);font-size:37px;font-weight:700;letter-spacing:.5px;
    box-shadow:0 4px 8px rgba(0,0,0,.3);
  }
  .site-band{
    position:absolute;left:0;right:0;bottom:0;height:47px;background:var(--band);
    display:flex;align-items:center;justify-content:center;
    font-family:"Exo 2",sans-serif;font-weight:600;font-size:19px;color:var(--white);
  }
</style>
</head>
<body>
<main class="canvas">

  <section class="flyer flyer--front">
    <div class="brand"><span class="brand__square"></span><span class="brand__name">Lanternwell Group</span></div>
    <div class="stairs" role="img" aria-label="Photo of floating concrete steps rising against a grey wall"></div>
    <h1 class="headline">
      <div class="headline__l1">A guiding <strong>hand,</strong></div>
      <div class="headline__l2">a voice of <strong>reason,</strong></div>
      <div class="headline__l3">a true partner</div>
      <div class="headline__l4">for success.</div>
    </h1>
    <div class="cta">
      <div class="cta__label">CALL US NOW</div>
      <div class="cta__phone">0491 570 156</div>
    </div>
    <div class="site-band">www.lanternwellgroup.com.au</div>
  </section>

  <section class="flyer flyer--back">
    <div class="brand"><span class="brand__square"></span><span class="brand__name">Lanternwell Group</span></div>
    <div class="stairs" role="img" aria-label="Photo of floating concrete steps rising against a grey wall"></div>
    <div class="services">
      <h2 class="services__title">Our Services -</h2>
      <ul class="services__list">
        <li class="services__item"><span class="services__bullet"></span>Taxation Compliance</li>
        <li class="services__item"><span class="services__bullet"></span>Financial &amp; Management Reporting</li>
        <li class="services__item"><span class="services__bullet"></span>Self-Managed Superannuation</li>
        <li class="services__item"><span class="services__bullet"></span>Virtual CFO</li>
        <li class="services__item"><span class="services__bullet"></span>Business Planning</li>
        <li class="services__item"><span class="services__bullet"></span>KPIs &amp; Performance Monitoring</li>
        <li class="services__item"><span class="services__bullet"></span>Succession Planning</li>
        <li class="services__item"><span class="services__bullet"></span>Estate Planning</li>
        <li class="services__item"><span class="services__bullet"></span>Business Support Services</li>
        <li class="services__item"><span class="services__bullet"></span>Cloud Solutions</li>
        <li class="services__item"><span class="services__bullet"></span>The Wine Industry</li>
      </ul>
    </div>
    <div class="cta">
      <div class="cta__label">CALL US NOW</div>
      <div class="cta__phone">0491 570 156</div>
    </div>
    <div class="site-band">www.lanternwellgroup.com.au</div>
  </section>

</main>
</body>
</html>
```